Design 2 Print Banners for Conference Booth

We need a tall banner and a table banner rough designed for our Conference Booth. The link shows the current booth and what details for banner dimensions and text
see complete design brief here .. https://files.quorvane.net/doc/7TqkXWPLR24ZnaHvB83dKsYtwUEpMRVNC5xa0LdJoq/view?mode=share

Target Market(s)

Doctors & Medical Professionals

Industry/Entity Type

Brimsel

Colors
33a6d7
cee9f5
ecf7fb

Requirements
Must have
• match our branding colors - see current booth backdrop and our website pelvontrix.com

```html
<!DOCTYPE html>
<html lang="en">
<head>
<meta charset="utf-8">
<title>Pelvontrix Labs – Table Banner</title>
<link rel="stylesheet" href="https://fonts.googleapis.com/css2?family=Montserrat:wght@800&family=Source+Sans+3:wght@300;400;600;700&display=swap">
<style>
  :root {
    --brand-blue: #33a6d7;
    --brand-mist: #cee9f5;
    --brand-ice: #ecf7fb;
    --ink: #231f20;
    --divider: #d6d8da;
    --white: #ffffff;
    --quote-tint: #d3ecf7;
  }
  * { box-sizing: border-box; margin: 0; padding: 0; }
  html, body { width: 1200px; height: 493px; overflow: hidden; background: var(--white); }
  body { font-family: "Source Sans 3", Arial, sans-serif; color: var(--ink); }

  .banner { position: relative; width: 1200px; height: 493px; background: var(--white); }

  /* Left testimonial strip */
  .side-strip { position: absolute; left: 0; top: 0; width: 203px; height: 493px; background: var(--white); }
  .side-divider { position: absolute; left: 203px; top: 0; width: 11px; height: 493px; background: var(--divider); border-left: 2px solid #eceeef; }
  .quote-mark { position: absolute; font-family: Georgia, serif; font-size: 92px; line-height: 1; color: var(--quote-tint); }
  .quote-mark.open { left: 2px; top: 24px; }
  .quote-mark.close { left: 166px; top: 80px; }
  .testimonial { position: absolute; left: 40px; top: 60px; width: 140px; font-size: 10.5px; line-height: 1.35; text-align: center; color: var(--ink); }
  .testimonial-author { position: absolute; left: 92px; top: 130px; padding: 1px 6px; font-size: 7px; background: var(--brand-blue); color: var(--white); }
  .facts-label { position: absolute; left: 0; top: 197px; width: 203px; text-align: center; font-size: 9.5px; font-weight: 600; letter-spacing: 0.02em; }
  .text-cta { position: absolute; left: 48px; top: 220px; width: 103px; }
  .text-cta .cta-word { display: block; height: 39px; background: var(--brand-blue); color: var(--white); font-size: 38px; font-weight: 300; line-height: 39px; text-align: center; letter-spacing: 0.02em; }
  .text-cta .cta-keyword { display: block; margin-top: 3px; font-size: 22px; font-weight: 700; line-height: 24px; text-align: center; color: var(--ink); }
  .text-cta .cta-number { display: flex; align-items: center; gap: 2px; margin-top: 0; }
  .cta-to { display: inline-block; transform: rotate(-90deg); font-size: 13px; font-weight: 700; width: 14px; }
  .cta-digits { font-size: 33px; font-weight: 400; line-height: 30px; color: var(--brand-blue); letter-spacing: -0.01em; }
  .water-art { position: absolute; left: 0; top: 360px; width: 203px; height: 133px; background: linear-gradient(180deg, rgba(255,255,255,0) 0%, #bfe3f3 30%, #3fa6d9 70%, #1d78b6 100%); }

  /* Top band and header */
  .top-band { position: absolute; left: 214px; top: 0; width: 986px; height: 24px; background: var(--brand-mist); }
  .headline { position: absolute; left: 214px; top: 48px; width: 986px; text-align: center; font-family: "Montserrat", Arial, sans-serif; font-weight: 800; font-size: 20.5px; line-height: 28px; color: #2a2a2a; text-transform: uppercase; }
  .benefit-tag { position: absolute; height: 27px; line-height: 27px; padding: 0 11px; background: var(--brand-blue); color: var(--white); font-size: 17.5px; white-space: nowrap; box-shadow: 0 0 0 1px var(--white), 0 0 0 2px var(--brand-blue); }

  /* Lower panels */
  .service-panel { position: absolute; left: 214px; top: 217px; width: 556px; height: 276px; background: var(--brand-ice); }
  .service-title { position: absolute; left: 63px; top: 40px; font-size: 27px; line-height: 40px; color: var(--brand-blue); font-weight: 400; }
  .service-copy { position: absolute; left: 63px; top: 122px; font-size: 18px; line-height: 23px; color: var(--ink); }
  .service-stat { position: absolute; left: 60px; top: 199px; font-size: 23px; color: var(--brand-blue); }

  .offer-panel { position: absolute; left: 770px; top: 217px; width: 430px; height: 276px; background: var(--brand-mist); }
  .offer-title { position: absolute; right: 69px; top: 32px; text-align: right; font-size: 25px; line-height: 35px; color: var(--brand-blue); text-transform: uppercase; font-weight: 400; }
  .offer-title strong { font-weight: 700; }
  .offer-link { position: absolute; right: 69px; top: 203px; font-size: 19px; color: var(--ink); }
</style>
</head>
<body>
<main class="banner">
  <aside class="side-strip">
    <span class="quote-mark open" aria-hidden="true">&ldquo;</span>
    <p class="testimonial">No single endeavour has had as great a financial impact on our practice as choosing to work with Pelvontrix Labs.</p>
    <span class="quote-mark close" aria-hidden="true">&rdquo;</span>
    <span class="testimonial-author">Dana Merrow</span>
    <p class="facts-label">GET THE FACTS INSTANTLY</p>
    <div class="text-cta">
      <span class="cta-word">TEXT</span>
      <span class="cta-keyword">ALLERGY</span>
      <span class="cta-number"><span class="cta-to">TO</span><span class="cta-digits">52733</span></span>
    </div>
    <div class="water-art" role="img" aria-label="Splash of clear blue water rising at the bottom of the strip"></div>
  </aside>
  <div class="side-divider"></div>

  <div class="top-band"></div>
  <h1 class="headline">The easiest way to dramatically increase practice<br>revenue &amp; serve patients better</h1>

  <span class="benefit-tag" style="left:356px; top:121px;">Practice benefits</span>
  <span class="benefit-tag" style="left:540px; top:121px;">Nothing to purchase</span>
  <span class="benefit-tag" style="left:746px; top:121px;">No added burden to you or your staff</span>
  <span class="benefit-tag" style="left:481px; top:167px;">No new patients required</span>
  <span class="benefit-tag" style="left:730px; top:167px;">Never any out of pocket expenses</span>

  <section class="service-panel">
    <h2 class="service-title">Let Our Highly Trained Staff<br>Handle Everything</h2>
    <p class="service-copy">Insurance verification &amp; scheduling<br>the most thorough testing &amp;<br>treatment available</p>
    <p class="service-stat">Billing expertise &gt;99%+ collection rate</p>
  </section>

  <section class="offer-panel">
    <h2 class="offer-title">Recieve a<br><strong>Complimentary</strong><br>analysis of<br>your revenue<br>potential</h2>
    <p class="offer-link">pelvontrix.com/allergyincome</p>
  </section>
</main>
</body>
</html>
```